Commercial Refrigeration Service Company requires stylish and fresh looking flyer.

We need a flyer to hand out to new customers. It should have a photo and our branding, list all the services that are offered and our contact details.
We would like two flyers to be supplied, both identical though one offering a discount until July ( Half Price Service Fee ). The flyer should be clear, interesting and in similar colours to the branding package supplied.
Please look at our website for information about the services on offer:
www.brambo-cooling.com.au

Target Market(s)

Cafes, bars, restaurants, pubs ect.

Font styles to use
Other font styles liked:
• Font package provided

Colors
85cae6
ffffff
333333

Requirements
Must have
• - The photo provided.
• - The company logo.
• - Similar feel to the website & business card.
• - Smooth layout and clear to understand.
Should not have
• - No clunky badges or prints.

```html
<!DOCTYPE html>
<html lang="en">
<head>
<meta charset="utf-8">
<title>Brambo Cooling – Services Flyer</title>
<link href="https://fonts.googleapis.com/css2?family=Montserrat:wght@700;800&family=Roboto+Condensed:wght@700&family=Raleway:wght@500&family=Dosis:wght@400;500&display=swap" rel="stylesheet">
<style>
  :root{
    --cyan:#85cae6;
    --cyan-bright:#7af0fb;
    --ink:#333333;
    --panel:#2d3033;
    --panel-light:#3a3e42;
    --white:#ffffff;
    --stage:#2b3033;
    --badge:#f7a51c;
    --badge-red:#d8202a;
  }
  *{margin:0;padding:0;box-sizing:border-box}
  html,body{width:1200px;height:1200px;overflow:hidden;background:var(--stage)}
  .flyer{position:absolute;left:200px;top:35px;width:800px;height:1130px;background:var(--panel);overflow:hidden}
  .flyer__shapes{position:absolute;inset:0}
  .services-title{position:absolute;left:55px;top:688px;font:800 30px/1 "Montserrat",sans-serif;color:var(--white);letter-spacing:.5px}
  .services-title span{color:var(--cyan-bright)}
  .service{position:absolute;width:220px;margin-left:-110px;text-align:center;color:var(--white)}
  .service svg{display:block;margin:0 auto 10px;width:52px;height:52px;fill:none;stroke:var(--white);stroke-width:3;stroke-linecap:round;stroke-linejoin:round}
  .service__label{font:700 15px/1.1 "Roboto Condensed",sans-serif;letter-spacing:.3px;text-transform:uppercase}
  .offer{position:absolute;left:470px;top:915px;width:290px;height:100px;background:var(--badge);border:2px dashed #1f1f1f;display:flex;align-items:center;gap:14px;padding:0 14px}
  .offer__tag{background:var(--badge-red);color:var(--white);font:800 24px/0.9 "Montserrat",sans-serif;padding:8px 10px;transform:rotate(-10deg)}
  .offer__text{font:500 28px/1.05 "Dosis",sans-serif;color:#1f1f1f}
  .footer{position:absolute;left:0;bottom:0;width:800px;height:105px;background:var(--white)}
  .brand{position:absolute;left:0;top:0;width:200px;height:105px}
  .brand__box{position:absolute;left:0;top:0;width:200px;height:56px;background:var(--cyan)}
  .brand__name{position:absolute;left:0;top:14px;width:200px;text-align:center;font:500 21px/1.5 "Raleway",sans-serif;letter-spacing:7px;color:var(--ink)}
  .contact-phone{position:absolute;left:225px;top:14px;font:800 34px/1 "Montserrat",sans-serif;color:var(--cyan-bright)}
  .contact-web{position:absolute;left:225px;top:60px;font:500 17px/1 "Dosis",sans-serif;color:var(--ink);letter-spacing:.3px}
  .contact-divider{position:absolute;left:478px;top:18px;height:58px;border-left:3px dotted var(--ink)}
  .contact-list{position:absolute;left:500px;top:16px;list-style:none;font:400 18px/1.55 "Dosis",sans-serif;color:var(--ink)}
  .contact-list li{display:flex;align-items:center;gap:10px}
  .contact-list svg{width:14px;height:14px;fill:var(--cyan-bright)}
</style>
</head>
<body>
<main class="flyer">
  <svg class="flyer__shapes" viewBox="0 0 800 1130" width="800" height="1130">
    <defs>
      <linearGradient id="photoTone" x1="0" y1="0" x2="0" y2="1">
        <stop offset="0" stop-color="#a9c9e3"/>
        <stop offset="0.35" stop-color="#8fa3b3"/>
        <stop offset="1" stop-color="#5b6166"/>
      </linearGradient>
    </defs>
    <rect class="photo" role="img" aria-label="Photo of the technician standing beside the branded service ute" x="0" y="0" width="800" height="700" fill="url(#photoTone)"/>
    <polygon class="panel-dark" points="0,300 0,1130 800,1130 800,150 440,650 410,680" fill="var(--panel)"/>
    <polygon class="panel-light" points="0,470 0,700 150,560" fill="var(--panel-light)"/>
    <path class="v-band" d="M0,170 L360,650 Q400,700 450,660 L800,190 L800,230 L455,690 Q400,760 345,690 L0,230 Z" fill="var(--cyan-bright)"/>
    <polygon class="accent-bar" points="610,650 650,610 800,720 800,800" fill="var(--cyan-bright)"/>
  </svg>

  <h2 class="services-title">OUR <span>SERVICES</span></h2>

  <div class="service" style="left:160px;top:770px">
    <svg viewBox="0 0 52 52"><path d="M18 8v30M6 23h24M9 14l18 18M27 14L9 32"/><rect x="34" y="10" width="8" height="26" rx="4"/><circle cx="38" cy="42" r="6"/></svg>
    <div class="service__label">Commercial Refrigeration</div>
  </div>
  <div class="service" style="left:360px;top:760px">
    <svg viewBox="0 0 52 52"><path d="M10 6h32l-4 40H14z"/><rect x="17" y="22" width="9" height="9"/><rect x="25" y="28" width="9" height="9"/></svg>
    <div class="service__label">Ice Makers</div>
  </div>
  <div class="service" style="left:530px;top:745px">
    <svg viewBox="0 0 52 52"><path d="M18 8h16v8h-6v30h-6V16h-4z"/></svg>
    <div class="service__label">Beer Systems</div>
  </div>
  <div class="service" style="left:685px;top:730px">
    <svg viewBox="0 0 52 52"><path d="M30 4L16 28h10l-6 20 16-26H26z" fill="#fff"/></svg>
    <div class="service__label">Electrical</div>
  </div>

  <div class="service" style="left:150px;top:925px">
    <svg viewBox="0 0 52 52"><path d="M44 22A19 19 0 0 0 10 14M8 30a19 19 0 0 0 34 8"/><path d="M8 6v9h9M44 46v-9h-9"/><text x="26" y="31" text-anchor="middle" font-family="Montserrat,sans-serif" font-weight="800" font-size="13" fill="#fff" stroke="none">24h</text></svg>
    <div class="service__label">24H Service</div>
  </div>
  <div class="service" style="left:290px;top:915px">
    <svg viewBox="0 0 52 52"><path d="M4 8h8l4 24h26l4-18H14"/><circle cx="19" cy="42" r="3"/><circle cx="39" cy="42" r="3"/></svg>
    <div class="service__label">Sales</div>
  </div>
  <div class="service" style="left:385px;top:905px">
    <svg viewBox="0 0 52 52"><path d="M10 42l30-30M36 6l10 10M8 10l34 34M6 14l8-8"/></svg>
    <div class="service__label">Installations</div>
  </div>

  <aside class="offer">
    <div class="offer__tag">half<br>price</div>
    <div class="offer__text">Service Fee<br>until June</div>
  </aside>

  <footer class="footer">
    <div class="brand">
      <div class="brand__box"></div>
      <div class="brand__name">BRAMBO<br>COOLING</div>
    </div>
    <div class="contact-phone">0400 127 480</div>
    <div class="contact-web">www.brambo-cooling.com.au</div>
    <div class="contact-divider"></div>
    <ul class="contact-list">
      <li><svg viewBox="0 0 14 14"><path d="M7 0a5 5 0 0 1 5 5c0 4-5 9-5 9S2 9 2 5a5 5 0 0 1 5-5zm0 3a2 2 0 1 0 0 4 2 2 0 0 0 0-4z"/></svg>PO Box 1180 Seabay NSW 2099</li>
      <li><svg viewBox="0 0 14 14"><circle cx="7" cy="7" r="7"/></svg>info@brambo-cooling.com.au</li>
    </ul>
  </footer>
</main>
</body>
</html>
```